web site for Biblical Oils, Candles and Perfumes

To make a web design with "magento".
To show image of the company/products and to be a shop.
see sample:
www.morvatlu.ws
it is important that we will have pages of description of the products category
then puctures with item description and option to select how many to add to the cart.
Special reduction on product or full category.
Managing clients with possibility to give special reduction to specific client.
each product can be see in bigger image.
can write more information about the product.

Target Market(s)

christian, evangelist, bible lover, belivers

Industry/Entity Type

It Company

Number of Pages Required

5+ page

Requirements
Must have
• my possibility to maintains the web-site by myself (wordpree workers)
Nice to have
• to have statitics

```html
<!DOCTYPE html>
<html lang="en">
<head>
<meta charset="utf-8">
<title>Morvatlu – Biblical Oils, Candles and Perfumes</title>
<link href="https://fonts.googleapis.com/css2?family=Open+Sans:wght@400;600;700&family=Lora:wght@500;700&display=swap" rel="stylesheet">
<style>
:root{
  --navy:#0b3466;
  --blue:#1a5ea8;
  --sky:#3d8fd6;
  --pale:#e8f2fb;
  --ink:#2b3a4a;
  --muted:#6d7b89;
  --line:#d6e1ec;
  --white:#ffffff;
  --price:#1d62a8;
  --lav1:#b9c9ec;
  --lav2:#7c79c2;
}
*{box-sizing:border-box;margin:0;padding:0}
html,body{width:1200px;height:2208px;overflow:hidden}
body{font-family:"Open Sans",Arial,sans-serif;color:var(--ink);background:var(--white);position:relative;font-size:12px}
.wrap{width:896px;margin:0 auto;position:relative}
/* header */
.site-header{height:180px;background:linear-gradient(180deg,#0a2e5c 0%,#1b5ca3 70%,#3b88d2 100%)}
.site-header .wrap{height:148px}
.brand{position:absolute;left:0;top:28px;display:flex;align-items:center;gap:10px;color:var(--white);font-size:30px;font-weight:700}
.brand i{width:14px;height:14px;border-radius:50%;background:var(--white);display:block}
.search{position:absolute;left:316px;top:28px;width:230px;height:28px;background:var(--white);border-radius:3px;display:flex;align-items:center;padding:0 10px;color:#9aa7b4;font-size:11px;justify-content:space-between}
.top-links{position:absolute;right:0;top:10px;color:#cfe1f4;font-size:10px;letter-spacing:.5px}
.cart{position:absolute;right:0;top:46px;display:flex;align-items:center;gap:8px;color:var(--white);font-size:13px}
.main-nav{position:absolute;left:0;top:148px;width:896px;height:32px;background:var(--white);display:flex;border-radius:3px 3px 0 0}
.main-nav a{flex:0 0 auto;padding:0 22px;line-height:32px;font-size:10.5px;font-weight:700;color:var(--navy);text-decoration:none;letter-spacing:.4px}
.main-nav a.active{background:var(--blue);color:var(--white)}
/* hero */
.hero{position:relative;height:380px;background:linear-gradient(180deg,#9fc9ee 0%,#d6e7f7 45%,var(--lav1) 70%,var(--lav2) 100%)}
.hero-copy{position:absolute;left:36px;top:50px;width:360px}
.hero-copy h1{font-family:"Lora",Georgia,serif;font-size:44px;color:var(--navy);font-weight:700}
.hero-copy h2{font-family:"Lora",Georgia,serif;font-size:22px;color:var(--blue);font-weight:500;margin-top:4px}
.hero-copy p{font-size:11px;color:var(--ink);margin-top:12px;line-height:1.5}
.btn{display:inline-block;background:var(--blue);color:var(--white);font-size:10px;font-weight:700;padding:6px 14px;border-radius:3px;letter-spacing:.5px;line-height:1.3}
.hero-copy .btn{margin-top:14px}
.hero-product{position:absolute;right:60px;top:60px;width:300px;height:230px;background:linear-gradient(135deg,#d9eadf,#9fbf9a);border-radius:4px}
/* promos */
.promos{display:flex;gap:12px;margin-top:12px}
.promo{flex:1;height:158px;border:1px solid var(--line);border-radius:3px;padding:16px;position:relative;background:linear-gradient(180deg,#fff,#f2f7fc)}
.promo h3{font-size:15px;color:var(--navy);font-weight:600;width:140px;line-height:1.25}
.promo p{font-size:9.5px;color:var(--muted);width:130px;margin:6px 0 12px;line-height:1.4}
.promo .shot{position:absolute;right:14px;top:24px;width:120px;height:110px;border-radius:3px}
.shot-candle{background:linear-gradient(135deg,#f1e4bd,#c9a35b)}
.shot-oil{background:linear-gradient(135deg,#dbe6f3,#8aa6c9)}
.shot-perfume{background:linear-gradient(135deg,#f6e6c2,#d4a441)}
/* about */
.about{display:flex;gap:30px;margin-top:30px;height:410px}
.categories{width:218px;border:1px solid var(--line);border-radius:3px;overflow:hidden;align-self:flex-start;flex:0 0 218px}
.categories h4{background:var(--blue);color:var(--white);font-size:12px;padding:9px 12px;letter-spacing:.5px}
.categories li{list-style:none;font-size:10px;color:var(--ink);padding:8px 12px;border-top:1px solid var(--line);display:flex;justify-content:space-between}
.categories li::after{content:"›";color:var(--blue)}
.about-copy h2{font-family:"Lora",Georgia,serif;font-size:24px;color:var(--navy);margin-bottom:10px}
.about-copy p{font-size:10.5px;line-height:1.6;color:var(--ink);margin-bottom:10px}
/* latest */
.latest{position:absolute;left:0;top:1190px;width:1200px;height:380px;background:linear-gradient(180deg,#2f7fce 0%,#5aa4e4 55%,#c3def5 100%)}
.ribbon{width:260px;height:34px;margin:0 auto;background:var(--navy);color:var(--white);text-align:center;line-height:34px;font-weight:700;letter-spacing:1.5px;font-size:13px;border-radius:0 0 4px 4px}
.cards{display:flex;gap:24px;margin-top:40px}
.card{width:160px;background:var(--white);border-radius:3px;overflow:hidden;box-shadow:0 2px 6px rgba(0,0,0,.15)}
.card .shot{height:150px;margin:10px 20px 0;border-radius:3px}
.card .name{font-size:11px;font-weight:700;color:var(--navy);text-align:center;margin-top:8px}
.card .desc{font-size:8.5px;color:var(--muted);text-align:center;margin:3px 8px 8px}
.card .bar{display:flex;background:var(--price);color:var(--white);height:28px;align-items:center}
.card .bar span{flex:1;font-size:14px;font-weight:700;padding-left:12px}
.card .bar b{width:40px;height:28px;background:var(--navy);display:flex;align-items:center;justify-content:center}
.t1{background:linear-gradient(135deg,#e8eef6,#9fb3cf)}
.t2{background:linear-gradient(135deg,#f3e6c6,#c9a35b)}
.t3{background:linear-gradient(135deg,#f5ecd8,#b89a6a)}
.t4{background:linear-gradient(135deg,#f7e9b8,#d8b23f)}
.t5{background:linear-gradient(135deg,#f2e2c4,#b7894a)}
/* best */
.best{position:absolute;left:0;top:1600px;width:1200px}
.best h2{display:flex;align-items:center;justify-content:center;gap:16px;font-size:16px;color:var(--navy);letter-spacing:1.5px}
.best h2::before,.best h2::after{content:"";width:70px;height:1px;background:var(--blue)}
.best-grid{display:flex;gap:40px;margin-top:30px}
.bcard{width:194px}
.bcard .shot{height:170px;border-radius:3px;margin:0 22px}
.b1{background:linear-gradient(135deg,#fbe9e6,#e3b3ad)}
.b2{background:linear-gradient(135deg,#fbf0c0,#e0b52f)}
.b3{background:linear-gradient(135deg,#e6f1fa,#8fb7da)}
.b4{background:linear-gradient(135deg,#faf1d9,#d9b66c)}
.bcard .name{font-size:12px;font-weight:700;color:var(--navy);margin-top:12px;text-align:center}
.bcard .desc{font-size:9px;color:var(--muted);margin:4px 0 10px;line-height:1.4;text-align:center}
.bcard .buy{display:flex;align-items:center;justify-content:space-between}
.bcard .price{font-size:16px;font-weight:700;color:var(--price)}
/* footer */
.site-footer{position:absolute;left:0;top:2040px;width:1200px;height:168px;background:linear-gradient(180deg,#0b3466,#082748);color:#c9d9ea}
.fcols{display:flex;gap:26px;padding-top:18px}
.fcol h5{color:var(--white);font-size:11px;letter-spacing:.6px;margin-bottom:8px}
.fcol li{list-style:none;font-size:9px;line-height:1.7}
.news{width:250px}
.news p{font-size:9px}
.news .field{display:flex;margin-top:8px}
.news .field div{width:170px;height:20px;background:var(--white);border-radius:2px 0 0 2px}
.news .field span{background:var(--sky);color:var(--white);font-size:9px;font-weight:700;padding:0 8px;line-height:20px}
.pay{display:flex;gap:5px;margin-top:10px}
.pay i{width:26px;height:16px;background:#d7e3ef;border-radius:2px;display:block}
.fbottom{position:absolute;left:0;bottom:10px;width:896px;display:flex;justify-content:space-between;font-size:8.5px}
.social{display:flex;gap:5px}
.social i{width:14px;height:14px;background:#3f6fa5;display:block;border-radius:2px}
</style>
</head>
<body>
<header class="site-header">
  <div class="wrap">
    <div class="brand"><i></i>Morvatlu</div>
    <div class="search">Search here...
      <svg width="12" height="12" viewBox="0 0 12 12"><circle cx="5" cy="5" r="3.8" fill="none" stroke="#1a5ea8" stroke-width="1.5"/><line x1="8" y1="8" x2="11" y2="11" stroke="#1a5ea8" stroke-width="1.5"/></svg>
    </div>
    <div class="top-links">HELP &nbsp;|&nbsp; LOGIN &nbsp;|&nbsp; MY ACCOUNT &nbsp;|&nbsp; SUPPORT</div>
    <div class="cart">
      <svg width="22" height="18" viewBox="0 0 22 18"><path d="M1 2h4l3 10h10l2-7H7" fill="none" stroke="#fff" stroke-width="1.6"/><circle cx="9" cy="15.5" r="1.6" fill="#fff"/><circle cx="17" cy="15.5" r="1.6" fill="#fff"/></svg>
      0 items
    </div>
    <nav class="main-nav">
      <a class="active">HOME</a><a>ABOUT US</a><a>PRODUCTS</a><a>BEST SELLING</a><a>RESOURCES</a><a>SUPPORT</a><a>CONTACT</a>
    </nav>
  </div>
</header>

<main class="wrap">
  <section class="hero" role="img" aria-label="Lavender field under a blue sky">
    <div class="hero-copy">
      <h1>Lavender Soap</h1>
      <h2>Soap for Your Beauty &amp; Health</h2>
      <p>Gentle natural soap made with pure oils from the Holy Land, kind to every skin type.</p>
      <span class="btn">SHOP NOW</span>
    </div>
    <div class="hero-product" role="img" aria-label="Olive oil soap bar with its box"></div>
  </section>

  <section class="promos">
    <div class="promo"><h3>Saint light of Salemra</h3><p>Hand poured candles with scents of the holy land.</p><span class="btn">BUY NOW</span><div class="shot shot-candle" role="img" aria-label="Candle gift set"></div></div>
    <div class="promo"><h3>Salem Vale</h3><p>Anointing oils pressed in the biblical tradition.</p><span class="btn">BUY NOW</span><div class="shot shot-oil" role="img" aria-label="Anointing oil bottles in a box"></div></div>
    <div class="promo"><h3>Light of Salemra</h3><p>Perfumes inspired by the spices of scripture.</p><span class="btn">BUY NOW</span><div class="shot shot-perfume" role="img" aria-label="Perfume box"></div></div>
  </section>

  <section class="about">
    <aside class="categories">
      <h4>OUR CATEGORY</h4>
      <ul>
        <li>Anointing Oils</li><li>Biblical Perfumes</li><li>Dead Sea Cosmetics</li><li>Holy Land Candles</li><li>Olive Oil Soap</li><li>Gift Sets</li><li>Home &amp; Decor</li><li>Incense</li><li>Jewelry</li><li>Special Offers</li>
      </ul>
    </aside>
    <div class="about-copy">
      <h2>Little About Morvatlu</h2>
      <p>Our small company is a leading maker of biblical oils, candles and perfumes, crafted in the Holy Land with care and faith for believers around the world.</p>
      <p>We offer anointing oils, olive oil soaps, Dead Sea salts, scented candles and gift sets, all made from pure natural ingredients following ancient recipes.</p>
      <p>Every item is blessed with a story from scripture, so you can bring the spirit of the land into your home, your prayer and your daily life.</p>
      <p>Our products are shipped worldwide with love and devotion.</p>
    </div>
  </section>
</main>

<section class="latest">
  <div class="ribbon">LATEST PRODUCTS</div>
  <div class="wrap">
    <div class="cards">
      <div class="card"><div class="shot t1" role="img" aria-label="Oil bottle gift box"></div><div class="name">Product Name</div><div class="desc">Short note about this item</div><div class="bar"><span>$47.58</span><b><svg width="14" height="12" viewBox="0 0 22 18"><path d="M1 2h4l3 10h10l2-7H7" fill="none" stroke="#fff" stroke-width="2"/></svg></b></div></div>
      <div class="card"><div class="shot t2" role="img" aria-label="Candle set box"></div><div class="name">Product Name</div><div class="desc">Short note about this item</div><div class="bar"><span>$47.58</span><b><svg width="14" height="12" viewBox="0 0 22 18"><path d="M1 2h4l3 10h10l2-7H7" fill="none" stroke="#fff" stroke-width="2"/></svg></b></div></div>
      <div class="card"><div class="shot t3" role="img" aria-label="Anointing oil box"></div><div class="name">Product Name</div><div class="desc">Short note about this item</div><div class="bar"><span>$47.58</span><b><svg width="14" height="12" viewBox="0 0 22 18"><path d="M1 2h4l3 10h10l2-7H7" fill="none" stroke="#fff" stroke-width="2"/></svg></b></div></div>
      <div class="card"><div class="shot t4" role="img" aria-label="Perfume gift box"></div><div class="name">Product Name</div><div class="desc">Short note about this item</div><div class="bar"><span>$47.58</span><b><svg width="14" height="12" viewBox="0 0 22 18"><path d="M1 2h4l3 10h10l2-7H7" fill="none" stroke="#fff" stroke-width="2"/></svg></b></div></div>
      <div class="card"><div class="shot t5" role="img" aria-label="Incense set"></div><div class="name">Product Name</div><div class="desc">Short note about this item</div><div class="bar"><span>$47.58</span><b><svg width="14" height="12" viewBox="0 0 22 18"><path d="M1 2h4l3 10h10l2-7H7" fill="none" stroke="#fff" stroke-width="2"/></svg></b></div></div>
    </div>
  </div>
</section>

<section class="best">
  <h2>BEST SELLINGS</h2>
  <div class="wrap">
    <div class="best-grid">
      <div class="bcard"><div class="shot b1" role="img" aria-label="Round soap bar"></div><div class="name">Product Name</div><div class="desc">Gentle natural product made with pure oils for daily care.</div><div class="buy"><span class="price">$ 25.99</span><span class="btn">BUY NOW</span></div></div>
      <div class="bcard"><div class="shot b2" role="img" aria-label="Soap bar with box"></div><div class="name">Product Name</div><div class="desc">Gentle natural product made with pure oils for daily care.</div><div class="buy"><span class="price">$ 25.99</span><span class="btn">BUY NOW</span></div></div>
      <div class="bcard"><div class="shot b3" role="img" aria-label="Perfume bottle"></div><div class="name">Product Name</div><div class="desc">Gentle natural product made with pure oils for daily care.</div><div class="buy"><span class="price">$ 25.99</span><span class="btn">BUY NOW</span></div></div>
      <div class="bcard"><div class="shot b4" role="img" aria-label="Gift pack"></div><div class="name">Product Name</div><div class="desc">Gentle natural product made with pure oils for daily care.</div><div class="buy"><span class="price">$ 25.99</span><span class="btn">BUY NOW</span></div></div>
    </div>
  </div>
</section>

<footer class="site-footer">
  <div class="wrap" style="height:168px">
    <div class="fcols">
      <div class="fcol news"><h5>NEWSLETTER SIGN UP</h5><p>Enter your email for our latest news</p><div class="field"><div></div><span>SUBMIT</span></div><div class="pay"><i></i><i></i><i></i><i></i></div></div>
      <div class="fcol"><h5>COMPANY</h5><ul><li>About Us</li><li>Product Range</li><li>Terms of Use</li><li>Order Now</li></ul></div>
      <div class="fcol"><h5>PRODUCTS</h5><ul><li>Best Sellers</li><li>New Arrivals</li><li>Gift Sets</li><li>Special Offers</li></ul></div>
      <div class="fcol"><h5>SUPPORT</h5><ul><li>FAQ</li><li>Privacy Policy</li><li>Shipping Info</li><li>Contact</li></ul></div>
      <div class="fcol"><h5>RESOURCES</h5><ul><li>Blog Updates</li><li>Scripture Notes</li><li>Gallery</li><li>Reviews</li></ul></div>
    </div>
    <div class="fbottom"><span>© 2024 www.morvatlu.ws · All rights reserved</span><div class="social"><i></i><i></i><i></i></div></div>
  </div>
</footer>
</body>
</html>
```